Slider created for Warm Kitchen Table

We need a new slider created for our Warm Kitchen Table website (www.warmkitchentable.com.au). Warm Kitchen Table is a central place where people who love food, cooking for their family and sharing recipes can hang out. We'd like the sliders to look more 'earthy' than the ones currently used - and more like our Facebook style https://www.facebook.com/WarmKitchenTable .
The first slider we'd like to create will point to the blog on the website with the following:
Text: In Season Now - Ruby Red Grapefruit
Image: Ruby Red Grapefruit
The slider is 990 X 225 pixels.

```html
<!DOCTYPE html>
<html lang="en">
<head>
<meta charset="utf-8">
<title>In Season Now – Ruby Red Grapefruit | Warm Kitchen Table</title>
<link rel="stylesheet" href="https://fonts.googleapis.com/css2?family=Montserrat:wght@400;500&family=Roboto+Slab:wght@400&display=swap">
<style>
  :root {
    --stage: #282828;
    --frame: #e6e2dc;
    --panel-red: #a0191c;
    --panel-red-deep: #8a1416;
    --headline-cream: #fbe7a6;
    --kicker-cream: #fdf3e0;
    --rule-cream: #f3e6d2;
    --button-top: #ffffff;
    --button-mid: #fdf1e2;
    --button-bottom: #f6b37a;
    --button-text: #1a1a1a;
    --photo-dark: #3a2214;
    --photo-warm: #b8552a;
  }
  html, body {
    margin: 0;
    padding: 0;
    width: 1200px;
    height: 818px;
    overflow: hidden;
    background: var(--stage);
  }
  .slider {
    position: absolute;
    left: 60px;
    top: 286px;
    width: 1080px;
    height: 245px;
    box-sizing: border-box;
    border: 1px solid var(--frame);
    display: flex;
    background: var(--panel-red);
  }
  .slider__photo {
    width: 549px;
    height: 100%;
    flex: none;
    background: linear-gradient(100deg, var(--photo-dark) 0%, var(--photo-warm) 100%);
  }
  .slider__panel {
    flex: 1;
    position: relative;
    background: radial-gradient(ellipse at 50% 45%, var(--panel-red) 0%, var(--panel-red-deep) 100%);
    text-align: center;
  }
  .kicker {
    position: absolute;
    top: 62px;
    left: 0;
    right: 0;
    display: flex;
    align-items: center;
    justify-content: center;
    gap: 10px;
    font-family: "Roboto Slab", Georgia, serif;
    font-size: 24px;
    letter-spacing: 1.5px;
    color: var(--kicker-cream);
    line-height: 1;
  }
  .kicker__rule {
    height: 2px;
    width: 84px;
  }
  .kicker__rule--left { background: linear-gradient(90deg, rgba(243,230,210,0), var(--rule-cream)); }
  .kicker__rule--right { background: linear-gradient(90deg, var(--rule-cream), rgba(243,230,210,0)); }
  .headline {
    position: absolute;
    top: 88px;
    left: 0;
    right: 0;
    margin: 0;
    font-family: "Montserrat", Arial, sans-serif;
    font-weight: 400;
    font-size: 45px;
    line-height: 1.2;
    color: var(--headline-cream);
    text-shadow: 1px 2px 3px rgba(60, 0, 0, 0.6);
  }
  .cta {
    position: absolute;
    top: 163px;
    left: 50%;
    transform: translateX(-50%);
    margin-left: 6px;
    width: 135px;
    height: 40px;
    box-sizing: border-box;
    border-radius: 3px;
    background: linear-gradient(180deg, var(--button-top) 0%, var(--button-mid) 50%, var(--button-bottom) 100%);
    box-shadow: 0 2px 4px rgba(40, 0, 0, 0.55);
    font-family: "Montserrat", Arial, sans-serif;
    font-weight: 500;
    font-size: 19px;
    line-height: 40px;
    color: var(--button-text);
    text-decoration: none;
  }
</style>
</head>
<body>
  <section class="slider">
    <div class="slider__photo" role="img" aria-label="Photograph of ruby red grapefruit in a stoneware bowl beside a jar of grapefruit marmalade on a rustic wooden table"></div>
    <div class="slider__panel">
      <div class="kicker">
        <span class="kicker__rule kicker__rule--left"></span>
        <span class="kicker__text">IN SEASON NOW</span>
        <span class="kicker__rule kicker__rule--right"></span>
      </div>
      <h1 class="headline">Ruby Red Grapefruit</h1>
      <a class="cta" href="#blog">Visit Blog</a>
    </div>
  </section>
</body>
</html>
```